Header für Blog zur Organisationsentwicklung
LunaKrie hat die Hinweise im Briefing und in den Kommentaren zu vorhandenen Designs gut aufgenommen und den Gestaltungsprozess vorangetrieben. So bekomme ich ein tolles Design, wo ich vorher keine Ahnung hatte, wie es aussehen sollte.
Zielgruppe
Ich bin freiberuflicher Organisationsberater und pflege auf meiner Website ein Blog zur Organisationsentwicklung. Dieses Blog soll zukünftig auf einer eigenen Domain erscheinen, sodass auch andere Kollegen sich daran beteiligen können. Daher soll mein Name nicht mehr im Vordergrund stehen - wenngleich ich immer noch als der Macher des Blog erkennbar bleiben soll.
Aufgabenstellung
Für das Blog "Labor für Unternehmenswandel" www.uw-labor.de wird ein ansprechender Header gesucht.
Der Header sollte den Namen des Blog und ein grafisches Element enthalten, dass der Bildsprache "Werkstatt", "Organisation", "Führung", etc. entnommen ist. Eventuell ein Element, das die Bildsprachen verbindet?
Da das Blog von einem Foto-Slider unter dem Header geprägt ist, sollte der Header nicht einfach aus einem Foto bestehen.
Die Farbgebung des Blog stellt die grafische Verbindung zu meiner Website www.hasselkamp.com her.
Mein Logo sollte im Header nicht verwendet werden, da ich das Blog bewusst von meiner Website löse, um weitere Beraterkollegen einzuladen, dabei mitzumachen

```html
<!DOCTYPE html>
<html lang="de">
<head>
<meta charset="utf-8">
<title>Labor für Unternehmenswandel – Header</title>
<link href="https://fonts.googleapis.com/css2?family=Open+Sans:wght@600&display=swap" rel="stylesheet">
<style>
  :root {
    --navy: #32336b;
    --navy-light: #55578a;
    --white: #ffffff;
  }
  html, body {
    margin: 0;
    padding: 0;
    overflow: hidden;
    background: var(--white);
  }
  .blog-header {
    position: relative;
    width: 1200px;
    height: 135px;
    background: var(--navy);
    overflow: hidden;
  }
  .blog-header__accent {
    position: absolute;
    inset: 0;
  }
  .blog-header__title {
    position: absolute;
    left: 54px;
    top: 0;
    height: 135px;
    margin: 0;
    display: flex;
    align-items: center;
    font-family: "Open Sans", sans-serif;
    font-weight: 600;
    font-size: 38px;
    letter-spacing: -0.2px;
    color: var(--white);
    padding-bottom: 4px;
    box-sizing: border-box;
  }
  .blog-header__icons {
    position: absolute;
    left: 0;
    top: 0;
  }
  .icon {
    fill: none;
    stroke: var(--white);
    stroke-width: 2.6;
    stroke-linecap: round;
    stroke-linejoin: round;
  }
</style>
</head>
<body>
<header class="blog-header">
  <svg class="blog-header__accent" width="1200" height="135" viewBox="0 0 1200 135" aria-hidden="true">
    <polygon points="945,0 1200,0 1200,135 857,135" fill="var(--navy-light)"/>
  </svg>

  <h1 class="blog-header__title">Labor für Unternehmenswandel</h1>

  <svg class="blog-header__icons" width="1200" height="135" viewBox="0 0 1200 135" aria-hidden="true">
    <!-- team -->
    <g class="icon icon--team">
      <circle cx="966" cy="50" r="8"/>
      <path d="M953 73 v-6 a9 9 0 0 1 9 -9 h9 a9 9 0 0 1 9 9 v14"/>
      <circle cx="941" cy="60" r="9"/>
      <path d="M924 94 v-16 a10 10 0 0 1 10 -10 h14 a10 10 0 0 1 10 10 v16 z"/>
    </g>
    <!-- sliders -->
    <g class="icon icon--sliders">
      <line x1="1010" y1="42" x2="1010" y2="92"/>
      <rect x="1005" y="55" width="10" height="9" rx="2"/>
      <line x1="1031" y1="42" x2="1031" y2="92"/>
      <rect x="1026" y="69" width="10" height="9" rx="2"/>
      <line x1="1052" y1="42" x2="1052" y2="92"/>
      <rect x="1047" y="58" width="10" height="9" rx="2"/>
    </g>
    <!-- growth bars -->
    <g class="icon icon--bars">
      <rect x="1084" y="80" width="9" height="12" rx="3"/>
      <rect x="1099" y="70" width="9" height="22" rx="3"/>
      <rect x="1114" y="57" width="9" height="35" rx="3"/>
      <rect x="1129" y="41" width="9" height="51" rx="3"/>
    </g>
  </svg>
</header>
</body>
</html>
```